Door Hanger Design

I need a design for a door hanger campaign. The door hanger will be 3.5" x 8.5" full color 2 sides. On the first side the emphasis is going to be house painting, exterior and interior. I would really like this to be bold and colorful, I would like to stay away from the standard here is what a painted house looks like.

For the 2nd side I would like the emphasis to be on kitchen and bathroom remodeling. One the front page of our website is a photo of one of our best jobs and if that could be incorporated into side 2 of the door hanger that would be awesome.

The name of our business is Dwelling Brightwell . Our website is http://dwelling-brightwell.example/. We don't currently have a company logo that we use.

I have never done this type of project before. So I'm sure I may be leaving some information out. If you need any questions answered please don't hesitate to contact me. They company that is going to print the designs said that I needed "camera ready artwork" and something about high resolution files.

Industry/Entity Type

House

```html
<!DOCTYPE html>
<html lang="en">
<head>
<meta charset="utf-8">
<title>Dwelling Brightwell Door Hangers</title>
<link rel="stylesheet" href="https://fonts.googleapis.com/css2?family=Arimo:wght@400;700&family=Oswald:wght@500;700&family=Roboto+Condensed:ital,wght@0,700;1,400;1,700&display=swap">
<style>
  :root {
    --paint-blue: #2b57b3;
    --paint-red: #e3262b;
    --paint-yellow: #ffd21c;
    --paint-orange: #f6a316;
    --ink: #111111;
    --grey: #8a8a8a;
    --brown-dark: #4a2e1f;
    --brown: #6b4630;
    --gold: #c99a3c;
    --cream: #fbf1d8;
    --beige: #e9c98a;
    --card-bg: #ffffff;
    --page: #ffffff;
  }
  * { box-sizing: border-box; margin: 0; padding: 0; }
  html, body { width: 848px; height: 1200px; overflow: hidden; background: var(--page); }
  body { position: relative; font-family: "Arimo", Arial, sans-serif; }

  .hanger {
    position: absolute;
    overflow: hidden;
    border-radius: 6px;
    box-shadow: 0 2px 6px rgba(0,0,0,.25);
  }
  .hanger-hole {
    position: absolute;
    width: 76px; height: 76px;
    border-radius: 50%;
    background: var(--page);
    z-index: 5;
  }
  .abs { position: absolute; }

  /* ---------- Painting side ---------- */
  .hanger-painting {
    left: 45px; top: 21px; width: 355px; height: 894px;
    background: linear-gradient(180deg, var(--paint-yellow) 0%, #ffc21a 45%, var(--paint-orange) 70%, #ffffff 71%);
  }
  .painting-art {
    left: 0; top: 0; width: 355px; height: 400px;
    background:
      linear-gradient(90deg, #2b63c9 0 22%, #f2f2f2 22% 38%, #3ab03e 38% 55%, #f2f2f2 55% 66%, #d7262c 66% 82%, #f2f2f2 82%) top / 100% 70px no-repeat,
      linear-gradient(170deg, #f4f4f4 0%, #fff7cf 30%, #ffd42a 55%, #fbb41a 100%);
  }
  .painting-side .hanger-hole { left: 141px; top: 82px; }
  .credit-badge { left: 191px; top: 248px; width: 146px; height: 146px; }
  .credit-badge svg { width: 100%; height: 100%; }
  .credit-text {
    left: 0; top: 0; width: 146px; height: 146px;
    display: flex; flex-direction: column; align-items: center; justify-content: center;
    color: #fff; text-align: center;
  }
  .credit-amount { font-family: "Arimo", Arial, sans-serif; font-weight: 700; font-size: 38px; line-height: 1; }
  .credit-label { font-family: "Arimo", Arial, sans-serif; font-weight: 700; font-size: 15px; margin-top: 3px; }

  .painting-kicker {
    left: 0; top: 405px; width: 355px; text-align: center;
    font-family: "Roboto Condensed", "Arial Narrow", sans-serif; font-weight: 700;
    font-size: 34px; color: var(--ink); letter-spacing: -0.5px;
  }
  .painting-title {
    left: 0; top: 438px; width: 355px; text-align: center;
    font-family: "Oswald", Impact, sans-serif; font-weight: 700;
    font-size: 72px; line-height: 1; color: var(--paint-blue); letter-spacing: 1px;
  }
  .painting-licensed {
    left: 0; top: 518px; width: 355px; text-align: center;
    font-family: "Arimo", Arial, sans-serif; font-size: 22px; color: var(--paint-red); letter-spacing: 1px;
  }
  .painting-offer {
    left: 26px; top: 554px; font-size: 14.5px; font-weight: 700; line-height: 1.25; color: var(--ink);
  }
  .offer-arrow { left: 222px; top: 550px; width: 62px; height: 40px; }
  .free-badge { left: 258px; top: 556px; width: 84px; height: 66px; }
  .free-badge svg { width: 100%; height: 100%; }
  .free-text {
    left: 0; top: 0; width: 84px; height: 66px;
    display: flex; align-items: center; justify-content: center;
    color: #fff; font-family: "Arimo", Arial, sans-serif; font-weight: 700; font-size: 17px;
  }
  .paint-cans {
    left: 0; top: 612px; width: 355px; height: 80px;
    background:
      linear-gradient(90deg, #c9cbd0 0 2%, transparent 2% 18%, #c9cbd0 18% 20%, transparent 20% 36%, #c9cbd0 36% 38%, transparent 38% 54%, #c9cbd0 54% 56%, transparent 56% 72%, #c9cbd0 72% 74%, transparent 74% 90%, #c9cbd0 90% 92%, transparent 92%),
      linear-gradient(180deg, #d9dde2 0%, #9ea3aa 35%, #e5e8ec 60%, #f7c4dd 85%, #ffffff 100%);
  }

  .contact-painting { left: 0; top: 700px; width: 355px; height: 105px; }
  .brand {
    position: absolute; display: flex; align-items: center; gap: 6px;
    font-family: "Arimo", Arial, sans-serif; font-weight: 400; font-size: 12px; color: var(--ink);
    white-space: nowrap;
  }
  .brand-square { width: 12px; height: 12px; background: var(--paint-orange); flex: none; }
  .contact-painting .brand { left: 12px; top: 46px; }
  .contact-name {
    position: absolute; font-family: "Arimo", Arial, sans-serif; font-weight: 700; color: var(--ink);
  }
  .contact-rule { position: absolute; height: 2px; }
  .contact-phone { position: absolute; font-family: "Arimo", Arial, sans-serif; color: var(--ink); }
  .contact-email { position: absolute; font-family: "Arimo", Arial, sans-serif; }
  .contact-painting .contact-name { left: 160px; top: 18px; font-size: 24px; }
  .contact-painting .contact-rule { left: 160px; top: 50px; width: 185px; background: var(--paint-red); }
  .contact-painting .contact-phone { left: 160px; top: 57px; font-size: 22px; letter-spacing: 1px; }
  .contact-painting .contact-email { left: 160px; top: 88px; font-size: 9.5px; color: var(--grey); }

  .painting-footer {
    left: 0; top: 811px; width: 355px; height: 83px;
    background: linear-gradient(180deg, var(--paint-red) 0 40px, #ffffff 40px 42px, var(--paint-blue) 42px 44px, #ef4b2e 44px);
  }
  .painting-url {
    left: 0; top: 8px; width: 355px; text-align: center;
    font-family: "Arimo", Arial, sans-serif; font-size: 20px; color: #fff; letter-spacing: .5px;
  }
  .card-row { position: absolute; display: flex; gap: 5px; }
  .card-badge { width: 36px; height: 22px; background: var(--card-bg); border: 1px solid #cfcfcf; border-radius: 2px; }
  .painting-footer .card-row { left: 108px; top: 51px; }

  /* ---------- Remodelling side ---------- */
  .hanger-remodel {
    left: 418px; top: 138px; width: 369px; height: 1007px;
    background: var(--cream);
  }
  .kitchen-photo {
    left: 0; top: 0; width: 369px; height: 540px;
    background:
      linear-gradient(180deg, #b68457 0%, #7c5334 22%, #d9c7a6 38%, #8e6a4c 55%, #5a3a25 75%, #8b5a36 100%);
  }
  .remodel-side .hanger-hole { left: 147px; top: 210px; }
  .remodel-title-band {
    left: 0; top: 533px; width: 369px; height: 120px;
    background: linear-gradient(180deg, #5b3a27 0%, var(--brown-dark) 100%);
  }
  .remodel-kicker {
    left: 0; top: 548px; width: 369px; text-align: center;
    font-family: "Roboto Condensed", "Arial Narrow", sans-serif; font-style: italic; font-weight: 400;
    font-size: 38px; color: #ffffff; letter-spacing: -0.5px;
  }
  .remodel-title {
    left: 0; top: 598px; width: 369px; text-align: center;
    font-family: "Oswald", Impact, sans-serif; font-weight: 700;
    font-size: 46px; line-height: 1; color: var(--gold); letter-spacing: 1.5px;
  }
  .remodel-list-panel {
    left: 0; top: 653px; width: 369px; height: 270px;
    background: linear-gradient(180deg, var(--beige) 0%, #f6e3b8 40%, var(--cream) 100%);
  }
  .service-list {
    left: 22px; top: 663px; list-style: none;
    font-family: "Arimo", Arial, sans-serif; font-weight: 700; font-size: 14.5px; color: var(--ink); line-height: 19px;
  }
  .service-list li { display: flex; align-items: center; gap: 8px; }
  .service-list svg { width: 10px; height: 10px; flex: none; }
  .remodel-more {
    left: 0; top: 798px; width: 340px; text-align: right;
    font-family: "Arimo", Arial, sans-serif; font-weight: 700; font-size: 15px; color: #8a5a2b;
  }
  .contact-remodel { left: 0; top: 820px; width: 369px; height: 100px; }
  .contact-remodel .brand { left: 14px; top: 42px; }
  .contact-remodel .brand-square { background: #e8742a; }
  .contact-remodel .contact-name { left: 160px; top: 12px; font-size: 24px; }
  .contact-remodel .contact-rule { left: 160px; top: 44px; width: 185px; background: var(--brown); }
  .contact-remodel .contact-phone { left: 160px; top: 52px; font-size: 22px; letter-spacing: 1px; }
  .contact-remodel .contact-email { left: 160px; top: 82px; font-size: 10.5px; color: var(--ink); }

  .remodel-footer {
    left: 0; top: 926px; width: 369px; height: 81px;
    background: linear-gradient(180deg, var(--brown) 0 34px, #ffffff 34px 36px, var(--brown-dark) 36px);
  }
  .remodel-url {
    left: 0; top: 6px; width: 369px; text-align: center;
    font-family: "Arimo", Arial, sans-serif; font-size: 20px; color: #fff; letter-spacing: .5px;
  }
  .remodel-licensed {
    left: 14px; top: 50px;
    font-family: "Arimo", Arial, sans-serif; font-size: 13px; color: #f1e3c8; letter-spacing: .5px;
  }
  .remodel-footer .card-row { left: 200px; top: 46px; }
  .remodel-footer .card-badge { width: 34px; height: 21px; }
</style>
</head>
<body>

<svg width="0" height="0" style="position:absolute" aria-hidden="true">
  <defs>
    <polygon id="starburst" points="100,50 91.2,58.2 96.2,69.2 84.9,73.4 85.4,85.4 73.4,84.9 69.2,96.2 58.2,91.2 50,100 41.8,91.2 30.8,96.2 26.6,84.9 14.6,85.4 15.1,73.4 3.8,69.2 8.8,58.2 0,50 8.8,41.8 3.8,30.8 15.1,26.6 14.6,14.6 26.6,15.1 30.8,3.8 41.8,8.8 50,0 58.2,8.8 69.2,3.8 73.4,15.1 85.4,14.6 84.9,26.6 96.2,30.8 91.2,41.8"/>
  </defs>
</svg>

<!-- Side one: painting -->
<section class="hanger hanger-painting painting-side">
  <div class="abs painting-art" role="img" aria-label="Bright paint drips in blue, green and red running down over a yellow paint roller stroke"></div>
  <div class="hanger-hole"></div>

  <div class="abs credit-badge">
    <svg viewBox="0 0 100 100"><use href="#starburst" fill="#ffffff"/><g transform="translate(6 6) scale(.88)"><use href="#starburst" fill="#2b57b3"/></g></svg>
    <div class="abs credit-text">
      <span class="credit-amount">$150</span>
      <span class="credit-label">Paint Credit</span>
    </div>
  </div>

  <p class="abs painting-kicker">Interior and Exterior</p>
  <h1 class="abs painting-title">PAINTING</h1>
  <p class="abs painting-licensed">Licensed and Insured</p>
  <p class="abs painting-offer">Driveway Pressure wash<br>with exterior painting</p>
  <svg class="abs offer-arrow" viewBox="0 0 62 40" aria-hidden="true">
    <polygon points="0,22 22,6 22,15 58,10 58,30 22,28 22,38" fill="#2b57b3" stroke="#ffffff" stroke-width="2"/>
  </svg>
  <div class="abs free-badge">
    <svg viewBox="0 0 100 100" preserveAspectRatio="none"><use href="#starburst" fill="#e3262b"/></svg>
    <div class="abs free-text">FREE!</div>
  </div>

  <div class="abs paint-cans" role="img" aria-label="Row of open silver paint cans filled with blue, pink, yellow and orange paint with colourful splatter"></div>

  <div class="abs contact-painting">
    <div class="brand"><span class="brand-square"></span>Dwelling Brightwell</div>
    <p class="contact-name">Marcus Delaney</p>
    <div class="contact-rule"></div>
    <p class="contact-phone">555-014-2760</p>
    <p class="contact-email">marcus@dwelling-brightwell.example</p>
  </div>

  <div class="abs painting-footer">
    <p class="abs painting-url">www.dwelling-brightwell.example</p>
    <div class="card-row" aria-label="Accepted payment cards">
      <span class="card-badge"></span><span class="card-badge"></span><span class="card-badge"></span><span class="card-badge"></span>
    </div>
  </div>
</section>

<!-- Side two: kitchen and bath remodelling -->
<section class="hanger hanger-remodel remodel-side">
  <div class="abs kitchen-photo" role="img" aria-label="Photo of a remodelled kitchen with wood ceiling, dark cabinets, island with bar stools and hardwood floor"></div>
  <div class="hanger-hole"></div>

  <div class="abs remodel-title-band"></div>
  <p class="abs remodel-kicker">Kitchen and Bath</p>
  <h2 class="abs remodel-title">REMODELLING</h2>

  <div class="abs remodel-list-panel"></div>
  <ul class="abs service-list">
    <li><svg viewBox="0 0 10 10"><polygon points="0,2 6,2 6,0 10,5 6,10 6,8 0,8" fill="#8a5a2b"/></svg>Repairs, Renovations, and Carpentry</li>
    <li><svg viewBox="0 0 10 10"><polygon points="0,2 6,2 6,0 10,5 6,10 6,8 0,8" fill="#8a5a2b"/></svg>Hardwood Floors, Floor and Wall Tiles</li>
    <li><svg viewBox="0 0 10 10"><polygon points="0,2 6,2 6,0 10,5 6,10 6,8 0,8" fill="#8a5a2b"/></svg>Appliance Installation</li>
    <li><svg viewBox="0 0 10 10"><polygon points="0,2 6,2 6,0 10,5 6,10 6,8 0,8" fill="#8a5a2b"/></svg>Door and Trim Installation</li>
    <li><svg viewBox="0 0 10 10"><polygon points="0,2 6,2 6,0 10,5 6,10 6,8 0,8" fill="#8a5a2b"/></svg>Counter Tops</li>
    <li><svg viewBox="0 0 10 10"><polygon points="0,2 6,2 6,0 10,5 6,10 6,8 0,8" fill="#8a5a2b"/></svg>Custom Cabinet and Closet</li>
  </ul>
  <p class="abs remodel-more">and a whole lot more....</p>

  <div class="abs contact-remodel">
    <div class="brand"><span class="brand-square"></span>Dwelling Brightwell</div>
    <p class="contact-name">Marcus Delaney</p>
    <div class="contact-rule"></div>
    <p class="contact-phone">555-014-2760</p>
    <p class="contact-email">marcus@dwelling-brightwell.example</p>
  </div>

  <div class="abs remodel-footer">
    <p class="abs remodel-url">www.dwelling-brightwell.example</p>
    <p class="abs remodel-licensed">Licensed and Insured</p>
    <div class="card-row" aria-label="Accepted payment cards">
      <span class="card-badge"></span><span class="card-badge"></span><span class="card-badge"></span><span class="card-badge"></span>
    </div>
  </div>
</section>

</body>
</html>
```